Bref créative
Business Card, Stationary, etc. for a plastic surgeon's office
Brennholt Clinic (Plastic & Reconstructive Surgery)
Use standard fonts
Play with the fonts to see what looks best.
Professional
Gregory T. Brennholt, DO
Plastic Surgeon
475 Corwin Haley Blvd, Ste. 260
Marlowe Shores, FL 30418
(Tollmead Business Park)
850-GET-TRIM (850-438-8746)
850-438-FAX5 (850-438-3295)
drbrennholt@brennholtclinic.example
www.brennholtclinic.example
This card, stationary, etc. should look clean and professional with my existing logo purchased from a designer using this sight.
I would like the back of the business card to contain the logo (i.e. Brennholt Clinic in larger letters with logo between the two words with Plastic & Reconstructive Surgery written below the main title with smaller font). Thanks and good luck!!!
logo vector file

```html
<!DOCTYPE html>
<html lang="en">
<head>
<meta charset="utf-8">
<title>Brennholt Clinic — Business Card</title>
<link rel="stylesheet" href="https://fonts.googleapis.com/css2?family=Raleway:wght@300;400;600&display=swap">
<style>
  :root {
    --backdrop: #e7e4df;
    --card-white: #ffffff;
    --gold: #c49a45;
    --gold-light: #e0c07c;
    --gold-deep: #b88d3a;
    --ink: #6f6a63;
    --ink-soft: #8d877f;
    --on-gold: #ffffff;
  }
  * { box-sizing: border-box; margin: 0; padding: 0; }
  html, body {
    width: 1200px; height: 787px; overflow: hidden;
    background: var(--backdrop);
    font-family: "Raleway", "Helvetica Neue", Arial, sans-serif;
  }
  .canvas { position: relative; width: 1200px; height: 787px; }

  .card {
    position: absolute;
    width: 520px; height: 300px;
    border-radius: 14px;
    box-shadow: 0 8px 24px rgba(0,0,0,0.12);
    overflow: hidden;
  }

  /* Front */
  .card-front { left: 50px; top: 150px; background: var(--card-white); color: var(--ink); }
  .card-front .brand { position: absolute; left: 0; right: 0; top: 46px; text-align: center; }
  .brand-name {
    font-weight: 400; font-size: 40px; letter-spacing: 1px; color: var(--gold);
    line-height: 1;
  }
  .brand-tagline {
    margin-top: 10px; font-weight: 400; font-size: 11px;
    letter-spacing: 3px; text-transform: uppercase; color: var(--gold);
  }
  .brand-rule { width: 300px; height: 1px; background: var(--gold-light); margin: 10px auto 0; }

  .contact { position: absolute; left: 150px; top: 160px; font-size: 11px; line-height: 1.55; }
  .person { font-size: 14px; margin-bottom: 8px; }
  .person-name { color: var(--gold); font-weight: 600; }
  .person-title { color: var(--ink-soft); }
  .person .divider { color: var(--ink-soft); margin: 0 6px; }
  .address { color: var(--ink-soft); }
  .phones { display: flex; gap: 16px; margin-top: 6px; color: var(--ink); }
  .phone-item { display: flex; align-items: center; gap: 5px; }
  .phone-item svg { width: 12px; height: 12px; }
  .email { margin-top: 4px; color: var(--ink-soft); }

  /* Back */
  .card-back {
    left: 630px; top: 330px;
    background: linear-gradient(135deg, var(--gold-light) 0%, var(--gold) 55%, var(--gold-deep) 100%);
    color: var(--on-gold);
  }
  .card-back .brand { position: absolute; left: 0; right: 0; top: 110px; text-align: center; }
  .card-back .brand-name { color: var(--on-gold); font-size: 44px; }
  .card-back .brand-tagline { color: var(--on-gold); }
  .card-back .brand-rule { background: rgba(255,255,255,0.7); width: 320px; }
  .web-rule { position: absolute; left: 90px; right: 90px; top: 246px; height: 1px; background: rgba(255,255,255,0.8); }
  .website {
    position: absolute; left: 0; right: 0; top: 256px; text-align: center;
    font-size: 13px; font-weight: 600; letter-spacing: 1.5px; color: var(--on-gold);
  }
</style>
</head>
<body>
<main class="canvas">
  <section class="card card-front" aria-label="Business card front">
    <div class="brand">
      <div class="brand-name">Brennholt Clinic</div>
      <div class="brand-rule"></div>
      <div class="brand-tagline">Plastic &amp; Reconstructive Surgery</div>
    </div>
    <div class="contact">
      <p class="person"><span class="person-name">Gregory T. Brennholt</span><span class="person-title">, DO</span><span class="divider">|</span><span class="person-title">Plastic Surgeon</span></p>
      <p class="address">475 Corwin Haley Blvd, Ste. 260</p>
      <p class="address">Marlowe Shores, FL 30418 (Tollmead Business Park)</p>
      <div class="phones">
        <span class="phone-item">
          <svg viewBox="0 0 12 12" aria-hidden="true"><circle cx="6" cy="6" r="6" fill="#c49a45"/><path d="M4 3.2c.4 0 .6.9.7 1.3.1.3-.5.6-.4.9.3.7.8 1.2 1.4 1.5.3.1.6-.5.9-.4.4.1 1.3.3 1.3.7 0 .6-.6 1.1-1.2 1C4.9 8 3.6 6.6 3.1 4.9c-.2-.7.3-1.7.9-1.7z" fill="#fff"/></svg>
          555-438-8746
        </span>
        <span class="phone-item">
          <svg viewBox="0 0 12 12" aria-hidden="true"><rect width="12" height="12" rx="2" fill="#c49a45"/><rect x="3" y="5" width="6" height="4" fill="#fff"/><rect x="4" y="2.5" width="4" height="2.5" fill="#fff"/></svg>
          555-438-3295
        </span>
      </div>
      <p class="email">drbrennholt@brennholtclinic.example</p>
    </div>
  </section>

  <section class="card card-back" aria-label="Business card back">
    <div class="brand">
      <div class="brand-name">Brennholt Clinic</div>
      <div class="brand-rule"></div>
      <div class="brand-tagline">Plastic &amp; Reconstructive Surgery</div>
    </div>
    <div class="web-rule"></div>
    <p class="website">www.brennholtclinic.example</p>
  </section>
</main>
</body>
</html>
```